15 ft high by 10 ft wide road side sign

road side sign - this is a dual carrigeway speeds of 40 mph so eye time to see ,read and absorb very short is less than 3 seconds 45,000 vehicles a day go past these are local to us our most profitable business is customers instore we embroider company and club and school logos and badges one mile ahead of this sign we have over 400,000 logos we have sewn and are on our servers we are well know in our area we can sew your logo in under 2 hours if it is already on our server we have a fast track service which we charge extra for very profitable is the customers buying items on vortiq and shopnu we can really be fast on your own items if you bring them instore we have 15 large multi head machine to cope no one else is that fast on line embroidery takes 7 -10 days we have purchased from others saying 24 hours when put to the test they fail and give excusses why it cannot be do every time we have brought and our customers say the same project your logo embrodery one mile ahead ------- road side sign 15 ft high 10 feet wide company name Swift Thread & Stitchworks 12 Harrowgate Close KT7 4PD like drivers to be able to drop off and collect sameday because driving you have very very little time to read has to be simple good thing is its a major commutor route A10 Enfield so drivers can be trained via repeat reading dale finch

Target Market(s)

our local area is our most profitable market getting people instore online is to slow to for our custopmers and low a margin for us 1,000,000 people withing 2 miles of our store

Industry/Entity Type

Embroidery

Font styles to use
Sans Serif

Colors

Designer to choose colors to be used in the design.

Requirements
Must have
• simple easy to read
• also
• nigel parsons lovers he has NP sewn on his union jack boxer shorts
• as clothing with your company logo are 100% tax deductable for most companies
• as promotional wear
Should not have
• to complicated to read and understand so many people driving past are not english readers as there main language

```html
<!DOCTYPE html>
<html lang="en">
<head>
<meta charset="utf-8">
<title>Swift Thread &amp; Stitchworks – Roadside Sign</title>
<link href="https://fonts.googleapis.com/css2?family=Arimo:wght@700&display=swap" rel="stylesheet">
<style>
  :root {
    --page-bg: #eef0f2;
    --sign-border: #ffffff;
    --band-red: #f40f12;
    --band-purple: #3b2a80;
    --band-green: #0e6b3b;
    --text-white: #ffffff;
    --edge-shadow: rgba(0, 0, 0, 0.25);
  }
  * { box-sizing: border-box; margin: 0; padding: 0; }
  html, body {
    width: 1200px;
    height: 788px;
    overflow: hidden;
    background: var(--page-bg);
  }
  .canvas {
    position: relative;
    width: 1200px;
    height: 788px;
  }
  .road-sign {
    position: absolute;
    left: 353px;
    top: 24px;
    width: 494px;
    height: 740px;
    border: 8px solid var(--sign-border);
    border-radius: 20px;
    overflow: hidden;
    box-shadow: 0 0 0 2px var(--edge-shadow);
    display: flex;
    flex-direction: column;
    font-family: "Arimo", Arial, sans-serif;
    font-weight: 700;
    color: var(--text-white);
    text-align: center;
    white-space: nowrap;
  }
  .band-name-top {
    background: var(--band-red);
    height: 196px;
    display: flex;
    flex-direction: column;
    align-items: center;
    justify-content: center;
    font-size: 86px;
    line-height: 0.98;
    letter-spacing: 1px;
  }
  .band-name-bottom {
    background: var(--band-purple);
    height: 138px;
    display: flex;
    flex-direction: column;
    align-items: center;
    justify-content: center;
    font-size: 56px;
    line-height: 1.05;
  }
  .band-message {
    flex: 1;
    background: var(--band-green);
    display: flex;
    flex-direction: column;
    align-items: center;
    justify-content: space-evenly;
    padding: 8px 10px 14px;
  }
  .message-service {
    font-size: 48px;
    line-height: 1.08;
  }
  .message-distance {
    display: flex;
    align-items: center;
    gap: 10px;
  }
  .distance-text {
    font-size: 56px;
    line-height: 1.05;
  }
  .arrow-down { width: 42px; height: 50px; flex: none; }
  .message-address {
    display: flex;
    align-items: center;
    gap: 10px;
  }
  .address-text {
    font-size: 34px;
    line-height: 1.3;
    text-decoration: underline;
    text-decoration-thickness: 3px;
    text-underline-offset: 5px;
  }
  .pin-icon { width: 32px; height: 46px; flex: none; }
  .line { display: block; }
</style>
</head>
<body>
  <main class="canvas">
    <section class="road-sign" aria-label="Swift Thread and Stitchworks roadside sign">
      <div class="band-name-top">
        <span class="line">SWIFT</span>
        <span class="line">THREAD</span>
      </div>
      <div class="band-name-bottom">
        <span class="line">&amp;</span>
        <span class="line">STITCHWORKS</span>
      </div>
      <div class="band-message">
        <p class="message-service">
          <span class="line">YOUR LOGO</span>
          <span class="line">EMBROIDERY</span>
        </p>
        <div class="message-distance">
          <svg class="arrow-down" viewBox="0 0 54 62" aria-hidden="true">
            <path d="M19 0h16v32h19L27 62 0 32h19z" fill="#ffffff"/>
          </svg>
          <p class="distance-text">
            <span class="line">ONE MILE</span>
            <span class="line">AHEAD</span>
          </p>
          <svg class="arrow-down" viewBox="0 0 54 62" aria-hidden="true">
            <path d="M19 0h16v32h19L27 62 0 32h19z" fill="#ffffff"/>
          </svg>
        </div>
        <div class="message-address">
          <svg class="pin-icon" viewBox="0 0 50 70" aria-hidden="true">
            <path d="M25 3C13 3 4 12 4 24c0 16 21 42 21 42s21-26 21-42C46 12 37 3 25 3z" fill="none" stroke="#ffffff" stroke-width="7"/>
            <circle cx="25" cy="24" r="7" fill="#ffffff"/>
          </svg>
          <p class="address-text">
            <span class="line">12 Harrowgate Close</span>
            <span class="line">KT7 4PD</span>
          </p>
        </div>
      </div>
    </section>
  </main>
</body>
</html>
```